Business Card Design Project: Classically Trained Singer and Voice Teacher

I am a classically trained singer that performs in Opera and Musical Theater and also teaches private voice lessons in those fields. I am looking for a business card that I can give to casting directors and colleagues, as well as to people who are interested in taking voice lessons from me.

This is sort of like an actors business card so I want my headshot and name to be the main focus.

I was kind of thinking of having the business card be horizontal with my headshot photo on the front taking up roughly half and my information on the same side, and perhaps my name again on the back or some form of my initials. But I am totally open to other options for layout.I would prefer to have a double sided business card, but once again, its not essential.

I am looking for it to look and feel elegant artistic and professional, without looking feminine.

Because of the colors of my headshot I would imagine that it would be predominantly brown and white, but I am totally open to other approaches.feel totally free to crop my headshot so that it fits better into your overall design and layout.

It is highly likely that I will ask the winner of the design to create a flyer for marketing my voice lessons with a similar look.

If you have any questions or clarifications, please feel free to ask.

Target Market(s)

Opera and Musical theater casting directors, colleagues; potential voice lesson students

Industry/Entity Type

Marketing

Requirements
Must have
• These must feature prominently:
- (My Headshot (attached))
- Marlow Keaton (my name)

These dont need to be as prominent:
- Baritone
- Private Voice Teacher
- Opera and Musical Theater

Contact Info:
Phone: (530) 555-0147
Email: markeat@inboxly.example

Nice to have
• Double sided

```html
<!DOCTYPE html>
<html lang="en">
<head>
<meta charset="utf-8">
<title>Marlow Keaton – Baritone</title>
<link rel="stylesheet" href="https://fonts.googleapis.com/css2?family=Jost:wght@400;500&display=swap">
<style>
  :root {
    --card-bg: #000000;
    --gold: #f7b41c;
    --white: #ffffff;
    --rule: #e6e6e6;
    --photo-light: #b9b9b6;
    --photo-mid: #8a6a4c;
    --photo-dark: #6b4a30;
  }
  html, body {
    margin: 0;
    padding: 0;
    width: 720px;
    height: 1200px;
    overflow: hidden;
    background: var(--card-bg);
  }
  .card {
    position: relative;
    width: 720px;
    height: 1200px;
    background: var(--card-bg);
    font-family: "Jost", "Futura", sans-serif;
  }
  .headshot {
    position: absolute;
    left: 163px;
    top: 81px;
    width: 379px;
    height: 350px;
    background: linear-gradient(100deg, var(--photo-light) 0%, #a39c94 30%, var(--photo-mid) 60%, var(--photo-dark) 100%);
  }
  .name {
    position: absolute;
    left: 0;
    top: 452px;
    width: 720px;
    margin: 0;
    text-align: center;
    color: var(--gold);
    font-weight: 400;
    font-size: 58px;
    letter-spacing: 0.2em;
    text-indent: 0.2em;
    line-height: 1;
  }
  .rule {
    position: absolute;
    left: 81px;
    width: 560px;
    height: 1px;
    background: var(--rule);
  }
  .rule--top { top: 560px; }
  .rule--bottom { top: 880px; }
  .roles {
    position: absolute;
    left: 0;
    top: 612px;
    width: 720px;
    margin: 0;
    padding: 0;
    list-style: none;
    text-align: center;
    color: var(--white);
    font-size: 26px;
    letter-spacing: 0.24em;
    text-indent: 0.24em;
  }
  .roles li {
    height: 80px;
    line-height: 36px;
  }
  .contact {
    position: absolute;
    left: 112px;
    top: 932px;
    margin: 0;
    padding: 0;
    list-style: none;
    color: var(--gold);
    font-size: 24px;
    letter-spacing: 0.18em;
  }
  .contact li {
    height: 80px;
    line-height: 36px;
  }
</style>
</head>
<body>
  <main class="card">
    <div class="headshot" role="img" aria-label="Headshot of the singer in a brown jacket and striped shirt"></div>
    <h1 class="name">MARLOW KEATON</h1>
    <div class="rule rule--top"></div>
    <ul class="roles">
      <li>BARITONE</li>
      <li>PRIVATE VOICE TEACHER</li>
      <li>OPERA &amp; MUSICAL THEATER</li>
    </ul>
    <div class="rule rule--bottom"></div>
    <ul class="contact">
      <li>Phone: (530) 555-0147</li>
      <li>Email: markeat@inboxly.example</li>
    </ul>
  </main>
</body>
</html>
```